Business Card Design

Business Card for professional consulting firm working with large financial institutions.

Target Market(s)

Executive buyers

Industry/Entity Type

Banking

Contact Information for Business Card

Mild creativity wanted. Not boring, but do elaborate artwork.

Font styles to use
Serif
Sans Serif

Colors

Designer to choose colors to be used in the design.

Requirements
Must have
• Standard business card features - company name, individual name, telephone, website, email, locations.
Nice to have
• Two colors
Should not have
• too many colors, fancy printing, cartoons.

```html
<!DOCTYPE html>
<html lang="en">
<head>
<meta charset="utf-8">
<title>Norvale Advisory – Business Card</title>
<link href="https://fonts.googleapis.com/css2?family=Tinos:wght@400;700&display=swap" rel="stylesheet">
<style>
  :root {
    --page: #2b2b2d;
    --card: #ffffff;
    --ink: #1a1a1a;
    --muted: #a8a8a8;
    --rule: #cfcfcf;
    --swoosh: #bdbdbd;
    --swoosh-light: #e6e6e6;
    --pattern-a: #f7f7f7;
    --pattern-b: #e9e9e9;
  }
  * { margin: 0; padding: 0; box-sizing: border-box; }
  html, body {
    width: 1200px; height: 906px; overflow: hidden;
    background: var(--page);
    font-family: "Tinos", "Times New Roman", serif;
    color: var(--ink);
  }
  .stage {
    width: 1200px; height: 906px;
    display: flex; flex-direction: column; align-items: center; justify-content: center;
    gap: 40px;
  }
  .card {
    position: relative;
    width: 700px; height: 400px;
    background: var(--card);
    border-radius: 28px;
    overflow: hidden;
  }
  /* back side */
  .card-back .pattern {
    position: absolute; inset: 0;
    background: linear-gradient(160deg, var(--pattern-a), var(--pattern-b));
  }
  .card-back .brand {
    position: absolute; right: 48px; bottom: 150px;
    display: flex; align-items: center; gap: 10px;
    font-size: 30px; color: var(--ink);
  }
  .brand .dot {
    width: 10px; height: 10px; border-radius: 50%; background: var(--swoosh);
  }
  /* front side */
  .card-front .swoosh { position: absolute; top: 0; right: 0; }
  .card-front .brand {
    position: absolute; left: 60px; top: 178px;
    display: flex; align-items: center; gap: 10px;
    font-size: 32px; color: var(--ink);
  }
  .divider {
    position: absolute; left: 372px; top: 135px;
    width: 1px; height: 140px; background: var(--rule);
  }
  .details { position: absolute; left: 400px; top: 128px; }
  .person-name { font-size: 29px; line-height: 1.1; }
  .person-role { font-size: 17px; color: var(--muted); margin-bottom: 12px; }
  .contact-list { list-style: none; }
  .contact-list li {
    display: flex; align-items: center; gap: 12px;
    font-size: 17px; line-height: 24px;
  }
  .contact-list svg { width: 15px; height: 15px; fill: none; stroke: var(--muted); stroke-width: 1.6; }
  .address {
    position: absolute; left: 0; right: 0; bottom: 48px;
    text-align: center; font-size: 18px;
  }
</style>
</head>
<body>
<main class="stage">
  <section class="card card-back">
    <div class="pattern" role="img" aria-label="Faint repeating brand-name pattern across the card"></div>
    <div class="brand"><span class="dot"></span>Norvale Advisory</div>
  </section>

  <section class="card card-front">
    <svg class="swoosh" width="330" height="120" viewBox="0 0 330 120" aria-hidden="true">
      <path d="M0 0 H330 V120 C300 60 230 30 120 22 C70 18 30 10 0 0 Z" fill="var(--swoosh-light)"/>
      <path d="M90 0 H330 V110 C310 55 250 25 160 12 C130 8 110 4 90 0 Z" fill="var(--swoosh)"/>
    </svg>

    <div class="brand"><span class="dot"></span>Norvale Advisory</div>
    <div class="divider"></div>

    <div class="details">
      <h1 class="person-name">Daniel R Ashby</h1>
      <p class="person-role">Business consultant</p>
      <ul class="contact-list">
        <li>
          <svg viewBox="0 0 16 16"><path d="M3 2 L6 2 L7 5 L5.5 6.5 C6.5 8.5 7.5 9.5 9.5 10.5 L11 9 L14 10 L14 13 C8 14 2 8 3 2 Z"/></svg>
          555-210-0147
        </li>
        <li>
          <svg viewBox="0 0 16 16"><rect x="1.5" y="3.5" width="13" height="9"/><path d="M1.5 3.5 L8 9 L14.5 3.5"/></svg>
          info@norvaleadvisory.com
        </li>
        <li>
          <svg viewBox="0 0 16 16"><circle cx="8" cy="8" r="6.5"/><ellipse cx="8" cy="8" rx="3" ry="6.5"/><path d="M1.5 8 H14.5"/></svg>
          www.norvaleadvisory.com
        </li>
      </ul>
    </div>

    <p class="address">PO Box 218, Kelmore QLD 4410</p>
  </section>
</main>
</body>
</html>
```